Re design my company logo boost my identity

Hello ,

i am asking for redesign and editing my logo to design a stationery for me
please don't ask many question just let your creativity kicks off .

don't change the logo 360 degree just boost it
my main color is Blue Light please be sure this color appear in your design very well
Blue Light = PANTONE 13-4909

Target Market(s)

young mens and girls 14 to 36 year old

Industry/Entity Type

It Company

Requirements
Must have
• my main color is Blue Light please be sure this color appear in your design very well
• Blue Light = PANTONE 13-4909

```html
<!DOCTYPE html>
<html lang="en">
<head>
<meta charset="utf-8">
<title>Lumora Letterhead</title>
<link href="https://fonts.googleapis.com/css2?family=Open+Sans:ital,wght@0,400;0,700;1,700&family=Dancing+Script:wght@500&display=swap" rel="stylesheet">
<style>
  :root {
    --backdrop: #6b6b6b;
    --paper: #ffffff;
    --ink: #1c1c1c;
    --ink-soft: #333333;
    --blue-light: #52c3d6;
    --accent-black: #0c0c0c;
  }
  * { box-sizing: border-box; margin: 0; padding: 0; }
  html, body {
    width: 1200px; height: 1000px; overflow: hidden;
    background: var(--backdrop);
    font-family: "Open Sans", Arial, sans-serif;
  }
  .letterhead {
    position: absolute; left: 282px; top: 48px;
    width: 636px; height: 904px;
    background: var(--paper);
    box-shadow: 0 4px 14px rgba(0,0,0,.35);
    overflow: hidden;
  }
  .brand {
    position: absolute; left: 50px; top: 44px;
    display: flex; align-items: center; gap: 10px;
  }
  .brand-dot {
    width: 30px; height: 30px; border-radius: 50%;
    background: var(--blue-light);
  }
  .brand-name {
    font-size: 30px; font-weight: 400; color: var(--blue-light);
    letter-spacing: 1px;
  }
  .date {
    position: absolute; right: 48px; top: 120px;
    font-size: 10.5px; font-weight: 700; color: var(--ink);
  }
  .recipient {
    position: absolute; left: 50px; top: 138px;
    font-size: 10px; font-weight: 700; font-style: italic;
    color: var(--ink); line-height: 22px;
  }
  .body-copy {
    position: absolute; left: 50px; top: 240px; width: 536px;
    font-size: 10px; line-height: 19px; color: var(--ink-soft);
    text-align: justify;
  }
  .body-copy p { text-indent: 12px; margin-bottom: 19px; }
  .closing {
    position: absolute; left: 50px; top: 630px;
    font-size: 10px; color: var(--ink-soft);
  }
  .signature {
    position: absolute; left: 50px; top: 656px;
    font-family: "Dancing Script", cursive;
    font-size: 34px; color: var(--ink);
  }
  .signatory {
    position: absolute; left: 50px; top: 718px;
    font-size: 10px; color: var(--ink-soft);
  }
  .contact-bar {
    position: absolute; left: 46px; top: 808px;
    display: flex; gap: 34px;
    font-size: 7.5px; color: var(--ink-soft);
  }
  .contact-item { display: flex; align-items: center; gap: 5px; }
  .contact-item svg { width: 8px; height: 8px; fill: var(--blue-light); }
  .footer-band {
    position: absolute; left: 0; bottom: 0; width: 636px; height: 80px;
  }
</style>
</head>
<body>
  <main class="letterhead">
    <header class="brand">
      <span class="brand-dot"></span>
      <span class="brand-name">lumora</span>
    </header>

    <div class="date">Date: 00.00.00</div>

    <address class="recipient">
      To<br>
      Lorem Ipsum<br>
      Addressline sample text and address<br>
      Area Name, Area Code
    </address>

    <section class="body-copy">
      <p>A type specimen book. It has survived not only five centuries, but also the leap into electronic typesetting, remaining essentially unchanged. It was popularised in the 1960s with the release of Glyphvane sheets containing Lorem Ipsum passages, and more recently with desktop publishing software like Setwrightly Layout including versions of Lorem Ipsum.</p>
      <p>It is a long established fact that a reader will be distracted by the readable content of a page when looking at its layout. The point of using Lorem Ipsum is that it has a more-or-less normal distribution of letters, as opposed to using 'Content here, content here', making it look like readable English. Many desktop publish'lorem ipsum' will uncover many web sites still in their infancy. Various versions have evolved over the years, sometimes by accident, sometimes on purpose (injected humour and the like).</p>
      <p>Contrary to popular belief, Lorem Ipsum is not simply random text. It has roots in a piece of classical Latin literature from 45 BC, making it over 2000 years old. Edwin Hartley, a Latin professor at Westbrook College in Virginia, looked up one of the more obscure Latin words, consectetur, from a Lorem Ipsum passage, and going through the cites of the word in classical literature, discovered the undoubtable source. Lorem Ipsum comes from sections 1.10.32 and 1.10.33 of "de Finibus Bonorum et Malorum" (The Extremes of Good and Evil) by Varrenus, written in 45 BC. This book</p>
    </section>

    <div class="closing">Lorem Ipsum</div>
    <div class="signature">Signature</div>
    <div class="signatory">Lorem Ipsum is a dummy</div>

    <footer class="contact-bar">
      <span class="contact-item">
        <svg viewBox="0 0 10 10"><rect x="0" y="2" width="10" height="7" rx="1"/></svg>
        info@lumora.com
      </span>
      <span class="contact-item">
        <svg viewBox="0 0 10 10"><circle cx="5" cy="5" r="4.5"/></svg>
        www.lumora.com
      </span>
      <span class="contact-item">
        <svg viewBox="0 0 10 10"><path d="M5 0a3.5 3.5 0 0 1 3.5 3.5C8.5 6 5 10 5 10S1.5 6 1.5 3.5A3.5 3.5 0 0 1 5 0z"/></svg>
        00/55 Harbour Lane Greenfield City Name 0000
      </span>
    </footer>

    <svg class="footer-band" viewBox="0 0 636 80" preserveAspectRatio="none">
      <polygon points="0,34 430,68 430,80 0,80" fill="var(--blue-light)"/>
      <polygon points="438,50 636,60 636,80 432,80" fill="var(--accent-black)"/>
    </svg>
  </main>
</body>
</html>
```